Business card - Harbourline Stoneworks

Design a business card utilizing the given logo.
colors we like: Black, greys, Teal, blues.
Tri color card, horizontal orientation likely
Logo and name likely best on top.
Info on card:

Dennis Farrowby
#5 - 4180 Maple Ridge Blvd.
Surrey, B.C. V3K 2R9

778.555.0193
dennisfarrowby@brellnet.ca

Slogan: "Building Dreams"

We are a construction company that specializes in new home construction on the West coast of BC Canada. Open Concepts designs of high end homes.

```html
<!DOCTYPE html>
<html lang="en">
<head>
<meta charset="utf-8">
<title>Harbourline Stoneworks – Business Card</title>
<link rel="stylesheet" href="https://fonts.googleapis.com/css2?family=Michroma&family=Montserrat:wght@500;700&display=swap">
<style>
  :root {
    --backdrop: #7a7a7a;
    --card-white: #ffffff;
    --teal: #0dba9f;
    --teal-light: #5cc6b0;
    --ink: #111111;
    --text-light: #ffffff;
  }
  * { margin: 0; padding: 0; box-sizing: border-box; }
  html, body {
    width: 1200px; height: 1000px; overflow: hidden;
    background: var(--backdrop);
  }
  .canvas {
    position: relative; width: 1200px; height: 1000px;
    display: flex; align-items: center; justify-content: center;
  }
  .business-card {
    position: relative; width: 880px; height: 544px;
    background: var(--teal); overflow: hidden;
    box-shadow: 2px 3px 6px rgba(0,0,0,0.35);
  }
  .brand-band {
    height: 198px; background: var(--card-white);
    display: flex; align-items: center; justify-content: center; gap: 22px;
  }
  .brand-dot {
    width: 110px; height: 110px; border-radius: 50%; background: var(--ink);
  }
  .brand-rule { width: 3px; height: 118px; background: var(--ink); }
  .brand-name {
    font-family: "Montserrat", sans-serif; font-weight: 700;
    font-size: 40px; line-height: 1.05; color: var(--ink);
    letter-spacing: 1px; text-transform: uppercase;
  }
  .accent-circle {
    position: absolute; right: -120px; top: 210px;
    width: 390px; height: 390px; border-radius: 50%;
    background: var(--teal-light); opacity: 0.55;
  }
  .person {
    position: absolute; left: 469px; top: 236px; color: var(--text-light);
  }
  .person-name {
    font-family: "Michroma", sans-serif; font-size: 33px; letter-spacing: 1px;
  }
  .person-title {
    font-family: "Montserrat", sans-serif; font-weight: 500; font-size: 21px;
    margin-top: 6px;
  }
  .contact-list {
    position: absolute; left: 76px; top: 388px; list-style: none;
    font-family: "Montserrat", sans-serif; font-weight: 500; font-size: 23px;
    color: var(--text-light);
  }
  .contact-item {
    display: flex; align-items: center; gap: 12px; height: 32px;
  }
  .contact-icon { width: 22px; height: 22px; flex: none; }
</style>
</head>
<body>
<main class="canvas">
  <article class="business-card">
    <header class="brand-band">
      <span class="brand-dot" aria-hidden="true"></span>
      <span class="brand-rule" aria-hidden="true"></span>
      <span class="brand-name">Harbourline<br>Stoneworks</span>
    </header>

    <div class="accent-circle" aria-hidden="true"></div>

    <section class="person">
      <h1 class="person-name">Dennis Farrowby</h1>
      <p class="person-title">Managing Director</p>
    </section>

    <ul class="contact-list">
      <li class="contact-item">
        <svg class="contact-icon" viewBox="0 0 22 22" aria-hidden="true">
          <rect width="22" height="22" rx="4" fill="#fff"/>
          <path d="M7 5c1 0 2 2.5 2 3s-1 1-1 1.5 2 3.5 3.5 3.5c.5 0 1-1 1.5-1s3 1 3 2-1.5 2.5-3 2.5C9 16.5 5 12 5 8c0-1.5 1-3 2-3z" fill="#0dba9f"/>
        </svg>
        778.555.0193
      </li>
      <li class="contact-item">
        <svg class="contact-icon" viewBox="0 0 22 22" aria-hidden="true">
          <rect width="22" height="22" rx="4" fill="#fff"/>
          <rect x="5" y="7" width="12" height="8" rx="1" fill="none" stroke="#0dba9f" stroke-width="1.6"/>
          <path d="M5 7l6 5 6-5" fill="none" stroke="#0dba9f" stroke-width="1.6"/>
        </svg>
        dennisfarrowby@brellnet.ca
      </li>
      <li class="contact-item">
        <svg class="contact-icon" viewBox="0 0 22 22" aria-hidden="true">
          <rect width="22" height="22" rx="4" fill="#fff"/>
          <path d="M11 4a5 5 0 0 1 5 5c0 4-5 9-5 9s-5-5-5-9a5 5 0 0 1 5-5z" fill="#0dba9f"/>
          <circle cx="11" cy="9" r="2" fill="#fff"/>
        </svg>
        #5 - 4180 Maple Ridge Blvd. Surrey, B.C. V3K 2R9
      </li>
    </ul>
  </article>
</main>
</body>
</html>
```